Zelcor Stationary

Design the stationary of Zelcor Promotion Group.

Zelcor is a BTL company, BTL meaning "below the line". In other words Zelcor is a Promotional Marketing company (the company that design the brands promotional activities).

The design should transmit creativity, agility, boldness.

I need:
* Bis Card
* Letter head
* Envelopes, both vertical and horizontal (for legal size), and letter envelope
* Folders
* PPT template (Title page and regular page)
* CD slip (CD envelope)
* ID card (employee card)

And what ever else you want to throw in.
Updates

Guys,

Something I missed from the brief.   The predominat color should be RED.

Also, have fun and play with the exclamation mark (!) of the logo. 

Hi guys, more comments:

Remember that Zelcor is a "creativity" agency, not in the advertising side but on the promotional side, and that should reflect on the stationary.

 I want a bold design.  Bold and yet crisp.

 

Guys, i just uploaded the Logo in AI format.

I Also uploaded the actual Zelcor Bis Card, wich I like.  So I will like to see some designs with that bis card approach.

Guys, I am so sorry, but I notice in your last post that I upladed a wrong design ("13154_marketing_group_zelcor_brief225630.ai").  The problem was that I asked the designer the file in AI format and he send me thw wrong file, and since I dont have Illustrator I could not verify it.

The differences are minor, I just already ask him the correct one (similar to the EPS file).

Sorry                                   

Just post the correct AI file : "Zelcor Logo.ai"

Reason: I'm expecting more designs to choose from and also I wont be available tomorrow to decide.

Reason: Sorry guys, but we are not there yet!

Target Market(s)

Marketing directors, Marketing Managers

Industry/Entity Type

Legal

Requirements
Must have
• Must work with the logo attached.
The predominat color should be RED.
Play and have fun with the exclamation mark (!).
Should not have
• * No old fonts

Should not be:
* boring
* Informal
* rigid

```html
<!DOCTYPE html>
<html lang="en">
<head>
<meta charset="utf-8">
<title>Zelcor Promotion Group — Folder</title>
<link rel="stylesheet" href="https://fonts.googleapis.com/css2?family=Source+Sans+3:wght@400;600;700;800&family=Arimo:wght@700&display=swap">
<style>
  :root {
    --backdrop: #2b2b2d;
    --red: #e31e24;
    --red-deep: #d0181e;
    --paper-top: #e9e9e9;
    --paper-bottom: #c9c9c9;
    --band: #b9b9b9;
    --band-light: #c8c8c8;
    --ink: #2a2a2a;
    --ink-soft: #3c3c3c;
    --heading-light: #dcdcdc;
  }
  * { margin: 0; padding: 0; box-sizing: border-box; }
  html, body { width: 900px; height: 1200px; overflow: hidden; }
  body {
    position: relative;
    background: var(--backdrop);
    font-family: "Source Sans 3", "Myriad Pro", Arial, sans-serif;
    color: var(--ink);
  }
  .sheet { position: absolute; }

  /* Red outer cover with exclamation pattern area */
  .cover {
    background: var(--red);
    box-shadow: 0 2px 8px rgba(0,0,0,.5);
  }
  .cover .pattern {
    position: absolute; inset: 0;
    background: linear-gradient(180deg, var(--red) 0%, var(--red-deep) 100%);
  }
  .contact-band {
    position: absolute; left: 0; right: 0;
    background: var(--band-light);
    display: flex; align-items: center;
  }
  .contact-band .col { font-size: 8px; line-height: 10px; color: var(--ink-soft); }
  .contact-band .col b { color: var(--red); font-weight: 700; }
  .contact-band .company { font-weight: 600; font-size: 8.5px; }
  .contact-band .divider { width: 1px; background: #8a8a8a; align-self: center; }

  /* Light grey inside panel */
  .inside {
    background: linear-gradient(180deg, var(--paper-top) 0%, #dedede 45%, var(--paper-bottom) 100%);
    box-shadow: 0 2px 8px rgba(0,0,0,.5);
  }
  .logo-band {
    position: absolute; left: 0; right: 0;
    background: var(--band);
    display: flex; align-items: center; justify-content: flex-end;
  }
  .wordmark {
    display: flex; align-items: center;
    font-weight: 800; color: var(--ink); letter-spacing: -0.5px;
  }
  .wordmark .dot { border-radius: 50%; background: var(--red); }
  .headline {
    position: absolute; color: var(--red); font-weight: 400;
  }

  .label {
    position: absolute; left: 116px; top: 622px;
    font-family: "Arimo", Arial, sans-serif; font-weight: 700;
    font-size: 74px; color: var(--heading-light); letter-spacing: 1px;
  }

  /* Main spread */
  .spread-cover { left: 52px; top: 52px; width: 386px; height: 516px; }
  .spread-cover .contact-band { top: 401px; height: 66px; padding-left: 20px; }
  .spread-cover .divider { height: 18px; margin: 0 10px 0 0; }
  .spread-cover .col { margin-right: 10px; }
  .spread-cover .company { width: 102px; }

  .spread-inside { left: 438px; top: 52px; width: 386px; height: 516px; }
  .spread-inside .logo-band { top: 136px; height: 65px; padding-right: 30px; }
  .spread-inside .wordmark { font-size: 26px; gap: 5px; }
  .spread-inside .dot { width: 10px; height: 10px; }
  .spread-inside .headline { left: 60px; top: 206px; font-size: 27px; line-height: 31px; }

  .pocket { position: absolute; left: 436px; top: 396px; }

  /* Small front and back views */
  .back-cover { left: 89px; top: 762px; width: 290px; height: 388px; }
  .back-cover .contact-band { top: 302px; height: 47px; padding-left: 15px; }
  .back-cover .col { font-size: 6px; line-height: 7.5px; margin-right: 8px; }
  .back-cover .company { font-size: 6.2px; width: 76px; }
  .back-cover .divider { height: 14px; margin-right: 8px; }

  .front-cover { left: 459px; top: 764px; width: 289px; height: 386px; }
  .front-cover .logo-band { top: 102px; height: 49px; padding-right: 26px; }
  .front-cover .wordmark { font-size: 19px; gap: 4px; }
  .front-cover .dot { width: 8px; height: 8px; }
  .front-cover .headline { left: 44px; top: 154px; font-size: 19px; line-height: 23px; }
</style>
</head>
<body>

  <!-- Open folder spread -->
  <section class="sheet cover spread-cover" aria-label="Folder outer cover">
    <div class="pattern" role="img" aria-label="Repeating pattern of red exclamation marks"></div>
    <div class="contact-band">
      <div class="col company">Zelcor Promotion Group<br><span style="font-weight:400">Street, Region, Country<br>PO BOX 321</span></div>
      <div class="divider"></div>
      <div class="col"><b>P</b> +31 (6) 55 01 22 33<br><b>F</b> +31 (6) 55 01 44 55</div>
      <div class="divider"></div>
      <div class="col"><b>E</b> hello@zelcor.example<br><b>W</b> www.zelcor.example</div>
    </div>
  </section>

  <svg class="pocket" width="420" height="344" viewBox="0 0 420 344" aria-hidden="true">
    <defs>
      <linearGradient id="tabShade" x1="0" y1="0" x2="1" y2="0">
        <stop offset="0" stop-color="#cfcfcf"/>
        <stop offset="1" stop-color="#b5b5b5"/>
      </linearGradient>
    </defs>
    <polygon points="388,0 416,10 416,160 388,172" fill="url(#tabShade)"/>
    <polygon points="2,172 388,172 388,342 16,342" fill="#e31e24"/>
  </svg>

  <section class="sheet inside spread-inside" aria-label="Folder inside panel">
    <div class="logo-band">
      <div class="wordmark">zelcor<span class="dot"></span></div>
    </div>
    <p class="headline">Lorem Ipsum<br>is simply dummy</p>
  </section>

  <h1 class="label">Folder</h1>

  <!-- Back cover -->
  <section class="sheet cover back-cover" aria-label="Folder back cover">
    <div class="pattern" role="img" aria-label="Repeating pattern of red exclamation marks"></div>
    <div class="contact-band">
      <div class="col company">Zelcor Promotion Group<br><span style="font-weight:400">Street, Region, Country<br>PO BOX 321</span></div>
      <div class="divider"></div>
      <div class="col"><b>P</b> +31 (6) 55 01 22 33<br><b>F</b> +31 (6) 55 01 44 55</div>
      <div class="divider"></div>
      <div class="col"><b>E</b> hello@zelcor.example<br><b>W</b> www.zelcor.example</div>
    </div>
  </section>

  <!-- Front cover -->
  <section class="sheet inside front-cover" aria-label="Folder front cover">
    <div class="logo-band">
      <div class="wordmark">zelcor<span class="dot"></span></div>
    </div>
    <p class="headline">Lorem Ipsum<br>is simply dummy</p>
  </section>

</body>
</html>
```